Bright Ledger Advert Flyer for KOREMIViewpoints magazine

Bright Ledger need a 1 A4 Full Page color advertisement created for the upcoming issues featured in the printed magazine. https://www.koremiviewpoint.com/magazines/September2017/BigData/

Brightledger.com.au

Your trusted Data & Analytics Partner

Focused Data driven solutions & services provider
Proven experience and trusted technologies

Quorvante
VTL
Big Data
Cloud Architecture
Advanced Analytics

```html
<!DOCTYPE html>
<html lang="en">
<head>
<meta charset="UTF-8">
<title>Bright Ledger – Data &amp; Analytics Advert</title>
<link rel="stylesheet" href="https://fonts.googleapis.com/css2?family=Anton&family=Open+Sans:wght@400;600;700&display=swap">
<style>
  :root{
    --navy:#14234a;
    --navy-deep:#0d1a3a;
    --orange:#f26a21;
    --orange-light:#f7931e;
    --sky:#9fb8de;
    --sky-pale:#dde6f3;
    --white:#ffffff;
    --text:#1d2a4d;
    --grey:#5b6478;
  }
  *{margin:0;padding:0;box-sizing:border-box}
  html,body{width:764px;height:1200px;overflow:hidden;background:#fff}
  .advert{position:relative;width:764px;height:1200px;overflow:hidden;background:var(--white);font-family:"Open Sans",sans-serif;color:var(--text)}
  .hero-photo{position:absolute;left:0;top:0;width:764px;height:600px;
    background:linear-gradient(120deg,#f4f6fb 0%,#dbe4f2 30%,#8fa9d3 55%,#3f5f9c 78%,#1c2f63 100%)}
  .headline{position:absolute;left:52px;top:88px;font-family:"Anton",sans-serif;font-size:78px;line-height:0.98;color:var(--navy);text-transform:uppercase;letter-spacing:0.5px}
  .brand-band{position:absolute;left:0;top:0;width:764px;height:1200px}
  .brand{position:absolute;left:52px;top:600px;display:flex;align-items:center;gap:12px}
  .brand-mark{width:22px;height:22px;background:var(--navy)}
  .brand-name{font-size:46px;font-weight:700;color:var(--navy);letter-spacing:-1px}
  .brand-tagline{position:absolute;left:52px;top:660px;font-size:11px;font-weight:600;letter-spacing:3px;color:var(--orange)}
  .services{position:absolute;left:52px;top:702px;list-style:none;font-size:18px;font-weight:600;color:var(--navy)}
  .services li{display:flex;align-items:center;gap:12px;height:31px}
  .services .tick{width:16px;height:16px;flex:none}
  .recognition{position:absolute;left:476px;top:760px;width:238px;height:148px;border:2px solid var(--navy);background:#fff;text-align:center;padding:12px 14px}
  .recognition-title{font-size:15px;font-weight:700;color:var(--navy)}
  .recognition-sub{font-size:9px;color:var(--grey);margin-top:2px}
  .recognition-badge{width:120px;height:44px;margin:8px auto 6px;background:var(--navy)}
  .recognition-note{font-size:9px;color:var(--grey);line-height:1.3}
  .partners-title{position:absolute;left:52px;top:984px;font-size:19px;font-weight:700;color:var(--orange)}
  .partners{position:absolute;left:52px;top:1020px;display:flex;gap:34px;align-items:center}
  .partner{font-size:16px;font-weight:700;color:var(--navy)}
  .footer{position:absolute;left:0;top:1100px;width:764px;height:100px;background:var(--navy-deep)}
  .footer-accent{position:absolute;left:0;top:1090px;width:764px;height:10px;background:var(--orange)}
  .contacts{position:absolute;left:52px;top:1128px;display:flex;gap:44px;align-items:center;color:#fff;font-size:15px;font-weight:600}
  .contact{display:flex;align-items:center;gap:9px}
  .contact svg{width:22px;height:22px;flex:none}
</style>
</head>
<body>
<main class="advert">
  <div class="hero-photo" role="img" aria-label="Businessman in a suit touching a glowing data interface in front of a blue city skyline"></div>

  <svg class="brand-band" viewBox="0 0 764 1200" aria-hidden="true">
    <polygon points="0,560 764,470 764,1200 0,1200" fill="#ffffff"/>
    <polygon points="0,545 764,455 764,478 0,568" fill="#f26a21"/>
    <polygon points="0,570 764,480 764,486 0,576" fill="#f7931e"/>
  </svg>

  <h1 class="headline">Your<br>Trusted<br>Data &amp;<br>Analytics<br>Partner</h1>

  <div class="brand"><span class="brand-mark"></span><span class="brand-name">Bright Ledger</span></div>
  <div class="brand-tagline">DATA | INSIGHT | GROWTH</div>

  <ul class="services">
    <li><svg class="tick" viewBox="0 0 16 16"><path d="M2 8.5l4 4L14 3" fill="none" stroke="#f26a21" stroke-width="3"/></svg>Focused Data driven solutions &amp; services provider</li>
    <li><svg class="tick" viewBox="0 0 16 16"><path d="M2 8.5l4 4L14 3" fill="none" stroke="#f26a21" stroke-width="3"/></svg>Proven experience and trusted technologies</li>
    <li><svg class="tick" viewBox="0 0 16 16"><path d="M2 8.5l4 4L14 3" fill="none" stroke="#f26a21" stroke-width="3"/></svg>Quorvante</li>
    <li><svg class="tick" viewBox="0 0 16 16"><path d="M2 8.5l4 4L14 3" fill="none" stroke="#f26a21" stroke-width="3"/></svg>VTL</li>
    <li><svg class="tick" viewBox="0 0 16 16"><path d="M2 8.5l4 4L14 3" fill="none" stroke="#f26a21" stroke-width="3"/></svg>Big Data</li>
    <li><svg class="tick" viewBox="0 0 16 16"><path d="M2 8.5l4 4L14 3" fill="none" stroke="#f26a21" stroke-width="3"/></svg>Cloud Architecture</li>
    <li><svg class="tick" viewBox="0 0 16 16"><path d="M2 8.5l4 4L14 3" fill="none" stroke="#f26a21" stroke-width="3"/></svg>Advanced Analytics</li>
  </ul>

  <aside class="recognition">
    <div class="recognition-title">Bright Ledger</div>
    <div class="recognition-sub">as featured in KOREMIViewpoints</div>
    <div class="recognition-badge"></div>
    <div class="recognition-note">Named among top data analytics solution providers 2017</div>
  </aside>

  <div class="partners-title">Our Partners</div>
  <div class="partners">
    <span class="partner">Quorvante</span>
    <span class="partner">VTL</span>
    <span class="partner">Nordavik</span>
    <span class="partner">Cirrelle</span>
  </div>

  <div class="footer-accent"></div>
  <footer class="footer"></footer>
  <div class="contacts">
    <span class="contact"><svg viewBox="0 0 24 24"><circle cx="12" cy="12" r="12" fill="#f26a21"/><path d="M8 6l2.5 0 1 3-1.6 1.2a7 7 0 0 0 3.9 3.9L15 12.5l3 1V16a2 2 0 0 1-2 2A10 10 0 0 1 6 8a2 2 0 0 1 2-2z" fill="#fff"/></svg>1300 555 018</span>
    <span class="contact"><svg viewBox="0 0 24 24"><circle cx="12" cy="12" r="12" fill="#f26a21"/><circle cx="12" cy="12" r="6" fill="none" stroke="#fff" stroke-width="1.6"/><path d="M6 12h12M12 6c-3 3.5-3 8.5 0 12M12 6c3 3.5 3 8.5 0 12" fill="none" stroke="#fff" stroke-width="1.2"/></svg>www.Brightledger.com.au</span>
    <span class="contact"><svg viewBox="0 0 24 24"><circle cx="12" cy="12" r="12" fill="#f26a21"/><rect x="6" y="8" width="12" height="8" fill="none" stroke="#fff" stroke-width="1.6"/><path d="M6 8l6 5 6-5" fill="none" stroke="#fff" stroke-width="1.6"/></svg>hello@brightledger.com.au</span>
  </div>
</main>
</body>
</html>
```